The Duchess of Nestware is an online store specialising in all things for the home Bathroom, Kitchen,

I need a business card designed that is professional and elegant, yet not conservative. We will be wanting to brand the entire business and will have videos made where we will be interacting with the product, testing the products and basically creating an online interactive community for all those people interested in all things to do with the Home and the activities that take place in and around the home.

Target Market(s)

30-65yr old Men and Women who LOVE their Home and see it as their primary place of Happiness, their sanctuary!

Industry/Entity Type

Business

Contact Information for Business Card

www.duchessofnestware.example The Duchess Of Nestware-PO Box 58316, Marlow Flats, Auckland. NEW ZEALAND. info@duchessofnestware.example
Love your Home! Corinne Dale-Petrakou

Font styles to use
Decorative
Script

Colors
9bcb3b
33b8a4
85cae6
b7a5cd
eda3c7
e667a6
d2a4cc
fdf9cf
fee18a

Requirements
Must have
• Attractive colours. Must feel Elegant, yet simple. A font that is rounded without sharp edges. Organic feel to the card, something raw with texture.
Nice to have
• I like the logo deign that I gave in the photos, something feminine, but fun.
Should not have
• I dont like sharp edges, or linear design. I like organic, flowing, fractal type design. Something that looks beautiful in form when you look at it.

```html
<!DOCTYPE html>
<html lang="en">
<head>
<meta charset="utf-8">
<title>The Duchess of Nestware – Business Card</title>
<link rel="stylesheet" href="https://fonts.googleapis.com/css2?family=Alegreya+Sans:wght@700&family=Dancing+Script:wght@700&family=Parisienne&display=swap">
<style>
  :root {
    --sky: #85cae6;
    --blush: #e9a6cb;
    --rose: #e667a6;
    --name-blue: #3d9ac8;
    --white: #ffffff;
    --stage: #ececec;
  }
  * { margin: 0; padding: 0; box-sizing: border-box; }
  html, body { width: 1200px; height: 1200px; overflow: hidden; }
  body { background: var(--stage); position: relative; font-family: "Alegreya Sans", sans-serif; }

  .card { position: absolute; left: 180px; width: 840px; height: 480px; overflow: hidden; }
  .card-front { top: 102px; }
  .card-back { top: 654px; background: var(--sky); }

  .snowflake-pattern {
    position: absolute; inset: 0;
    background: linear-gradient(135deg, var(--sky) 0%, #b9d9ec 45%, var(--blush) 100%);
  }

  .name-panel {
    position: absolute; left: 246px; top: 64px; width: 348px; height: 348px;
    background: var(--white); border-radius: 24px;
    display: flex; align-items: center; justify-content: center;
  }
  .brand-name {
    font-family: "Alegreya Sans", sans-serif; font-weight: 700; font-size: 34px;
    color: var(--name-blue); line-height: 1.15; text-align: center;
  }

  .tagline {
    position: absolute; left: 0; width: 100%; top: 112px; text-align: center;
    font-family: "Parisienne", cursive; font-size: 48px; color: var(--rose);
  }
  .tagline-swoosh { position: absolute; left: 358px; top: 172px; width: 240px; height: 30px; }
  .owner-name {
    position: absolute; left: 0; width: 100%; top: 202px; text-align: center;
    font-family: "Dancing Script", cursive; font-weight: 700; font-size: 56px; color: var(--rose);
  }
  .divider { position: absolute; left: 60px; right: 52px; top: 304px; height: 1px; background: rgba(255,255,255,0.7); }
  .contact { position: absolute; top: 320px; font-size: 17px; color: var(--white); }
  .contact-web { left: 62px; }
  .contact-mail { right: 54px; }
  .address { position: absolute; left: 0; width: 100%; top: 410px; text-align: center; font-size: 17px; color: var(--white); }
</style>
</head>
<body>
  <section class="card card-front">
    <div class="snowflake-pattern" role="img" aria-label="Repeating pattern of white and pink snowflakes in hexagons on sky blue"></div>
    <div class="name-panel">
      <h1 class="brand-name">The Duchess<br>of Nestware</h1>
    </div>
  </section>

  <section class="card card-back">
    <p class="tagline">Love your Home!</p>
    <svg class="tagline-swoosh" viewBox="0 0 240 30" aria-hidden="true">
      <path d="M0,26 Q100,4 240,2 Q110,10 0,26 Z" fill="var(--white)"/>
    </svg>
    <p class="owner-name">Corinne Dale-Petrakou</p>
    <div class="divider"></div>
    <p class="contact contact-web">www.duchessofnestware.example</p>
    <p class="contact contact-mail">info@duchessofnestware.example</p>
    <p class="address">The Duchess Of Nestware-PO Box 58316,&nbsp; Marlow Flats, Auckland. NEW ZEALAND.</p>
  </section>
</body>
</html>
```